Company Stationary

I'd like a template to use for company stationery. We frequently write short 1 - 2 page Word documents (which we save as PDF) to clients and prospects and the presentation is boring and doesn't look professional. I am looking for a Word template that will convey a better sense of professionalism. The design should include our logo (attached) but be simple and elegant. It should save nicely as a PDF, since that is how we will send the files via email.

Target Market(s)

Financial Institutions

Industry/Entity Type

Financial Service

Font styles to use
Serif

Colors

Designer to choose colors to be used in the design.

Requirements
Must have
• Simple design. Needs to be subtle. I don't want the design to be more interesting than the message we are writing.
Nice to have
• When the reader sees it, I want them to feel they are reading something published by a large, very successful company.
Should not have
• Not overpowering design and colors.

```html
<!DOCTYPE html>
<html lang="en">
<head>
<meta charset="utf-8">
<title>Clearwell Letterhead</title>
<link href="https://fonts.googleapis.com/css2?family=Exo+2:wght@700&display=swap" rel="stylesheet">
<style>
  :root {
    --paper-top: #ffffff;
    --paper-bottom: #e3e3e3;
    --brand-red: #f01400;
    --brand-black: #111111;
    --ink: #1a1a1a;
  }
  html, body {
    margin: 0;
    padding: 0;
    overflow: hidden;
  }
  .letterhead {
    position: relative;
    width: 1079px;
    height: 1200px;
    overflow: hidden;
    background: linear-gradient(to bottom, var(--paper-top) 0%, #f4f4f4 40%, var(--paper-bottom) 100%);
  }
  .letterhead__brand {
    position: absolute;
    left: 92px;
    top: 62px;
    margin: 0;
    font-family: "Exo 2", sans-serif;
    font-weight: 700;
    font-size: 40px;
    letter-spacing: 1px;
    color: var(--ink);
    line-height: 1;
  }
  .letterhead__stripes {
    position: absolute;
    inset: 0;
    width: 1079px;
    height: 1200px;
  }
  .stripe--red { fill: var(--brand-red); }
  .stripe--black { fill: var(--brand-black); }
  .stripe--rule {
    fill: none;
    stroke: var(--brand-red);
    stroke-width: 2;
  }
</style>
</head>
<body>
  <main class="letterhead">
    <p class="letterhead__brand">Clearwell</p>
    <svg class="letterhead__stripes" viewBox="0 0 1079 1200" aria-hidden="true">
      <polygon class="stripe--red" points="952,0 985,0 985,640 960,685 952,685"/>
      <polygon class="stripe--black" points="1002,0 1020,0 1020,330 1008,352 1002,352"/>
      <polyline class="stripe--rule" points="1034,0 1034,640 1022,660 1022,1200"/>
    </svg>
  </main>
</body>
</html>
```